Are You Prepared? Know how to support your pre-natal, post-natal and family resilience

I wish to supply a manual (both hardcopy and digit/PDF file/e-booklet) to obstetricians for them to issue to expectant parents. Content will be on pre-natal, post-natal and family mental health tips. I'd like the manual to feel fresh/bright with an educational focus, not mental health stigma, in order to empower prospective parents to up skill and nurture their own resilience and that of their children. Some pages may require me to include content than others. I would also like the option of including illustrations/infographics/diagrams. Please make it compatible with Microsoft Publisher. Thank you for your efforts!!

Target Market(s)

Prospective and expectant parents, young families

Industry/Entity Type

Family Planning

Font styles to use
Serif

Colors

Designer to choose colors to be used in the design.

Requirements
Must have
• • Needed: A booklet template that I can edit content over time, add pages and manipulate the images/text boxes myself.
• • Final deliverables: title page, contents page and several [inner] page layouts that I am able to rotate. Variety in visual layouts so I may repeat combinations to form a manual of 20+ pages.
• • File formats: Microsoft Publisher preferred but PDF files can also be provided (native design files per PixelGuild standards if Publisher not used)
• © Psychologist, Mirela Kostandis
Nice to have
• Layouts similar to the ones attached
• For designers to gain context for the content, topics will include:
• - Perinatal depression - risk and protective factors
• - Birth process, plan and expectations
• - Realistic expectations to motherhood (recovery, feeding, sleep deprivation, heightened emotions, settling and unsettled baby, bonding, body image, managing priorities, partner dynamics and communication, filtering outside advice and managing family dynamics).
• - Transition of identity. Adjusting to change and fulfillment pendulum.
• Encouraging disclosure
• - Perfectionism, shame and sense of ‘maternal failure’
• - Family dynamics
• - Discipline methods, parent communication, behavioural habits
• - Partner experience - sensitivities, difficulties, support, community attitude, role expectation, bonding, relationship dynamic with partner and extended family.
• - Grandparent boundaries, assistance and transition
• - Medical professionals and perinatal mental health, evidence based info, efficiency
• - Digital screening, mental health first aid skills.
• - Travel
• - Health and special needs
• - Trauma, grief, loss. Miscarriage. Stillborn. Maternal / paternal health. Genetic issues. Fear of mobility and mortality
Should not have
• Mental illness/stigma visuals

```html
<!DOCTYPE html>
<html lang="en">
<head>
<meta charset="utf-8">
<title>Prenatal Care – Booklet Spread</title>
<link href="https://fonts.googleapis.com/css2?family=Open+Sans:wght@300;400;700&family=Source+Sans+3:wght@400;600&display=swap" rel="stylesheet">
<style>
  :root {
    --backdrop: #ffffff;
    --page-white: #fbfbfb;
    --page-grey-top: #dcdcdc;
    --page-grey-bottom: #f2f2f2;
    --ink: #2b2b2b;
    --ink-soft: #5a5a5a;
    --title: #ffffff;
    --photo-light: #e8d2a0;
    --photo-mid: #c9a15e;
    --photo-deep: #7f6233;
    --gutter-shade: rgba(0,0,0,0.10);
  }
  * { box-sizing: border-box; margin: 0; padding: 0; }
  html, body { width: 1200px; height: 900px; overflow: hidden; background: var(--backdrop); }
  .canvas { position: relative; width: 1200px; height: 900px; }
  .spread {
    position: absolute; left: 148px; top: 130px;
    width: 904px; height: 640px; display: flex;
    box-shadow: 0 6px 24px rgba(0,0,0,0.12);
  }
  .page { position: relative; width: 452px; height: 640px; overflow: hidden; font-family: "Source Sans 3", "Open Sans", sans-serif; color: var(--ink); }
  .page--left { background: linear-gradient(180deg, var(--page-grey-top) 45%, var(--page-grey-bottom) 100%); }
  .page--left::after { content: ""; position: absolute; right: 0; top: 0; width: 22px; height: 100%; background: linear-gradient(90deg, transparent, var(--gutter-shade)); }
  .page--right { background: var(--page-white); }
  .page--right::before { content: ""; position: absolute; left: 0; top: 0; width: 18px; height: 100%; background: linear-gradient(90deg, var(--gutter-shade), transparent); }

  .hero-photo {
    position: absolute; left: 0; top: 0; width: 452px; height: 292px;
    background:
      radial-gradient(ellipse at 35% 55%, var(--photo-deep) 0%, transparent 45%),
      linear-gradient(160deg, var(--photo-light) 0%, var(--photo-mid) 55%, var(--photo-deep) 100%);
  }
  .section-title {
    position: absolute; left: 48px; top: 42px;
    font-family: "Open Sans", sans-serif; font-size: 25px; letter-spacing: 0.5px;
    color: var(--title);
  }
  .section-title strong { font-weight: 700; }
  .section-title span { font-weight: 300; }

  .body-copy { position: absolute; font-size: 8.4px; line-height: 10.8px; text-align: justify; }
  .body-copy p { margin-bottom: 10px; }
  .page--left .body-copy { left: 95px; top: 338px; width: 282px; }
  .page--right .body-copy { left: 85px; top: 98px; width: 282px; }
  .visit-list { list-style: none; margin-bottom: 10px; }
  .visit-list li { position: relative; padding-left: 11px; }
  .visit-list li::before { content: "•"; position: absolute; left: 0; }

  .page-number { position: absolute; bottom: 18px; font-family: "Open Sans", sans-serif; font-weight: 300; font-size: 15px; color: var(--ink-soft); }
  .page--left .page-number { left: 46px; }
  .page--right .page-number { right: 46px; }
  .page-credit { position: absolute; bottom: 22px; font-size: 7.5px; color: var(--ink-soft); }
  .page--left .page-credit { right: 30px; }
  .page--right .page-credit { left: 38px; }
</style>
</head>
<body>
<div class="canvas">
  <div class="spread">
    <section class="page page--left">
      <div class="hero-photo" role="img" aria-label="Photo of an expectant mother sitting cross-legged in golden dry grass, hands resting on her belly"></div>
      <h1 class="section-title"><strong>PRENATAL</strong> <span>CARE</span></h1>
      <div class="body-copy">
        <p>Prenatal care, also known as antenatal care, is a type of preventive healthcare. Its goal is to provide regular check-ups that allow doctors or midwives to treat and prevent potential health problems throughout the course of the pregnancy and to promote healthy lifestyles that benefit both mother and child. During check-ups, pregnant women receive medical information over maternal physiological changes in pregnancy, biological changes, and prenatal nutrition including prenatal vitamins. Recommendations on management and healthy lifestyle changes are also made during regular check-ups. The availability of routine prenatal care, including prenatal screening and diagnosis, has played a part in reducing the frequency of maternal death, miscarriages, birth defects, low birth weight, neonatal infections and other preventable health problems.</p>
        <p>The Global Maternal Health Council (GMHC) reported that in 2015 around 830 women died every day from problems in pregnancy and childbirth. Only 5 lived in high-income countries. The rest lived in low-income countries.</p>
        <p>A study examined the differences in early and low-weight birth deliveries between local and immigrant women and saw the difference caused by prenatal care received. The study, between 1997 and 2008, looked at 21,708 women giving birth in a region of Spain. The results indicated that very preterm birth (VPTB) and very low birth weight (VLBW) were much more common for immigrants than locals (Ferrandis et al., 2012). The study showed the importance of prenatal care and how</p>
      </div>
      <div class="page-number">01</div>
      <div class="page-credit">© Psychologist, Mirela Kostandis</div>
    </section>

    <section class="page page--right">
      <div class="body-copy">
        <p>universal prenatal care would help people of all origins get proper care before pregnancy/birth (Ferrandis et al., 2012).</p>
        <p>The GMHC recommends that pregnant women should all receive four antenatal visits to spot and treat problems and give immunizations. Although antenatal care is important to improve the health of both mother and baby, many women do not receive four visits.</p>
        <p>There are many ways of changing health systems to help women access antenatal care, such as new health policies, educating health workers and health service reorganisation. Community interventions to help people change their behavior can also play a part. Examples of interventions are media campaigns reaching many people, enabling communities to take control of their own health, informative-education-communication interventions and financial incentives. A review looking at these interventions found that one intervention helps improve the number of women receiving antenatal care. However interventions used together may reduce baby deaths in pregnancy and early life, lower numbers of low birth weight babies born and improve numbers of women receiving antenatal care.</p>
        <p>Traditional prenatal care in high-income countries generally consists of:</p>
        <ul class="visit-list">
          <li>monthly visits during the first two trimesters (from the 1st week to the 28th week)</li>
          <li>fortnightly visits from the 28th week to the 36th week of pregnancy</li>
          <li>weekly visits after 36th week to the delivery, from the 38th week to the 42nd week</li>
          <li>Assessment of parental needs and family dynamics</li>
        </ul>
        <p>The traditional form of antenatal care has developed from the early 1900s and there is very little research to suggest that it is the best way of giving antenatal care.[6] Antenatal care can be costly and uses a lot of staff. The following paragraphs describe research on other forms of antenatal care, which may reduce the burden on maternity services in all countries.</p>
      </div>
      <div class="page-credit">© Psychologist, Mirela Kostandis</div>
      <div class="page-number">02</div>
    </section>
  </div>
</div>
</body>
</html>
```